Brantwell Group needs a business card design

We need a new business card design using the logo recently selected in a logo competition on Pixel Forum. Our business is a consultancy specializing in aviation and energy and the winning business card design will promote an image of precision and professionalism with creativity.

Please use the logo with the name on the front of the card and use a complementary font. Make the back white with either the light grey or dark grey logo.

Target Market(s)

Senior finance and legal leaders at aviation and energy companies

Industry/Entity Type

Management Consulting

Contact Information for Business Card

Peter Haldane
President
Brantwell Group

www.brantwellgroup.example

(555) 304-6198
ph@brantwellgroup.example

Requirements
Must have
• Professional font that goes well with the logo font

```html
<!DOCTYPE html>
<html lang="en">
<head>
<meta charset="utf-8">
<title>Brantwell Group – Business Card</title>
<link href="https://fonts.googleapis.com/css2?family=Questrial&display=swap" rel="stylesheet">
<style>
  :root {
    --backdrop: #d9d9d9;
    --paper: #f1f1f0;
    --stripe-blue: #2b4f9c;
    --stripe-navy: #0f1e3a;
    --brand-blue: #284a8c;
    --ink: #333638;
    --ink-soft: #55595c;
    --mark-faint: #b4b9cc;
  }
  * { margin: 0; padding: 0; box-sizing: border-box; }
  html, body { width: 1200px; height: 900px; overflow: hidden; }
  body {
    background: var(--backdrop);
    font-family: "Questrial", "Helvetica Neue", Arial, sans-serif;
    display: flex;
    align-items: center;
    justify-content: center;
    gap: 50px;
  }
  .card {
    position: relative;
    width: 525px;
    height: 300px;
    background: var(--paper);
    box-shadow: 0 2px 0 #e4e4e4, 0 4px 0 #dcdcdc, 0 10px 24px rgba(0,0,0,0.18);
  }
  .edge-stripe { position: absolute; left: 0; bottom: 0; width: 525px; height: 20px; }
  .card-back .brand-faint {
    position: absolute;
    top: 50%; left: 50%;
    transform: translate(-50%, -60%);
    display: flex; align-items: center; gap: 14px;
    color: var(--mark-faint);
    font-size: 34px;
    letter-spacing: 3px;
    white-space: nowrap;
  }
  .brand-faint .brand-dot { width: 26px; height: 26px; background: var(--mark-faint); }
  .card-front .brand {
    position: absolute;
    left: 48px; top: 58px;
    display: flex; align-items: center; gap: 10px;
    color: var(--brand-blue);
    font-size: 20px;
    letter-spacing: 2px;
    text-transform: uppercase;
  }
  .brand .brand-dot { width: 14px; height: 14px; background: var(--brand-blue); }
  .details {
    position: absolute;
    right: 34px; top: 118px;
    text-align: right;
    color: var(--ink);
  }
  .details .person-name { font-size: 21px; letter-spacing: 0.5px; margin-bottom: 2px; }
  .details .line { font-size: 12.5px; line-height: 16px; color: var(--ink-soft); }
  .contacts { margin-top: 16px; }
  .contact { display: flex; align-items: center; justify-content: flex-end; gap: 7px; font-size: 12.5px; line-height: 18px; color: var(--ink-soft); }
  .contact svg { width: 12px; height: 12px; fill: var(--brand-blue); }
</style>
</head>
<body>

  <section class="card card-back" aria-label="Card back">
    <div class="brand-faint"><span class="brand-dot"></span>Brantwell Group</div>
    <svg class="edge-stripe" viewBox="0 0 525 20" aria-hidden="true">
      <polygon points="0,2 196,2 210,14 210,20 0,20" fill="var(--stripe-blue)"/>
      <polygon points="0,2 0,8 196,8" fill="var(--stripe-blue)"/>
      <polygon points="200,2 525,2 525,20 214,20 214,13" fill="var(--stripe-navy)"/>
    </svg>
  </section>

  <section class="card card-front" aria-label="Card front">
    <div class="brand"><span class="brand-dot"></span>Brantwell Group</div>
    <div class="details">
      <p class="person-name">Peter J. Haldane</p>
      <p class="line">President</p>
      <p class="line">Brantwell Group LLC</p>
      <p class="line">Finance and Strategy Consulting</p>
      <p class="line">Aviation - Manufacturing - Energy</p>
      <div class="contacts">
        <p class="contact">
          <svg viewBox="0 0 24 24" aria-hidden="true"><path d="M6.6 10.8a15.1 15.1 0 0 0 6.6 6.6l2.2-2.2a1 1 0 0 1 1-.25 11.4 11.4 0 0 0 3.6.57 1 1 0 0 1 1 1V20a1 1 0 0 1-1 1A17 17 0 0 1 3 4a1 1 0 0 1 1-1h3.5a1 1 0 0 1 1 1c0 1.25.2 2.45.57 3.57a1 1 0 0 1-.25 1z"/></svg>
          (555) 304-6198
        </p>
        <p class="contact">
          <svg viewBox="0 0 24 24" aria-hidden="true"><path d="M2 5h20v14H2z M3.5 6.5 12 13l8.5-6.5" fill="var(--brand-blue)" stroke="var(--paper)" stroke-width="1.5"/></svg>
          ph@brantwellgroup.example
        </p>
      </div>
    </div>
    <svg class="edge-stripe" viewBox="0 0 525 20" aria-hidden="true">
      <polygon points="0,8 196,8 210,20 0,20" fill="var(--stripe-blue)"/>
      <polygon points="200,2 525,2 525,20 214,20 214,13" fill="var(--stripe-navy)"/>
    </svg>
  </section>

</body>
</html>
```